Brightwell Consulting Business Card Design

Business Card Design for Brightwell Consulting. Brightwell Consulting is a boutique consultancy based in Atlanta, GA., that specializes in marketing strategy, organization planning, and leadership development. We provide solutions for small businesses and startups as well as Summit 400 companies.

http://brightwellconsulting.example/

Target Market(s)

We provide solutions for small businesses and startups as well as Summit 400 companies.

Industry/Entity Type

Consulting

Contact Information for Business Card

Two sided business card with priority on contact information, logo, tag line (Inspiration to Plan Well, Lead Well, Grow Well)

Colors

Designer to choose colors to be used in the design.

Requirements
Must have
• contact information, logo, tag line (Inspiration to Plan Well, Lead Well, Grow Well)
• Simple no over communication.
Nice to have
• I would like to see different placements of logo and creative use of both sides of the card
Should not have
• Do not put too much information on the card.

```html
<!DOCTYPE html>
<html lang="en">
<head>
<meta charset="utf-8">
<title>Brightwell Consulting – Business Card</title>
<link href="https://fonts.googleapis.com/css2?family=Lato:ital,wght@0,400;0,700;1,400&display=swap" rel="stylesheet">
<style>
  :root {
    --page: #e9ebef;
    --navy-deep: #1b2f52;
    --navy: #243c64;
    --navy-band: #34507e;
    --paper: #ffffff;
    --ink: #1f3358;
    --icon: #8ea3c4;
    --text-light: #ffffff;
  }
  * { margin: 0; padding: 0; box-sizing: border-box; }
  html, body {
    width: 822px; height: 1200px; overflow: hidden;
    background: var(--page);
    font-family: "Lato", sans-serif;
  }
  .sheet {
    position: relative; width: 822px; height: 1200px;
    display: flex; flex-direction: column; align-items: center; justify-content: center;
    gap: 90px;
  }
  .card {
    position: relative; width: 700px; height: 400px; overflow: hidden;
    box-shadow: 0 8px 24px rgba(20, 35, 60, 0.25);
  }
  .card-art { position: absolute; inset: 0; width: 100%; height: 100%; }

  /* Contact side */
  .contact-row {
    position: absolute; left: 115px;
    color: var(--text-light); font-style: italic; font-size: 21px;
    line-height: 1; transform: translateY(-50%); white-space: nowrap;
  }
  .contact-row.email { top: 83px; }
  .contact-row.web { top: 159px; }
  .contact-row.phone { top: 237px; font-style: normal; font-size: 23px; letter-spacing: 0.5px; }

  .front-logo {
    position: absolute; right: 28px; bottom: 28px; text-align: right; color: var(--ink);
  }
  .logo-name { display: block; font-weight: 700; font-size: 42px; line-height: 1; }
  .logo-sub { display: block; font-weight: 700; font-size: 16px; letter-spacing: 2px; margin-top: 4px; }
  .front-tagline { display: block; font-size: 18px; margin-top: 8px; color: var(--ink); white-space: nowrap; }

  /* Brand side */
  .card.brand {
    background: radial-gradient(ellipse at 60% 30%, #2d4872 0%, var(--navy) 45%, var(--navy-deep) 100%);
    display: flex; flex-direction: column; align-items: center; justify-content: center;
    color: var(--text-light); text-align: center;
  }
  .brand .logo-name { font-size: 70px; }
  .brand .logo-sub { font-size: 24px; letter-spacing: 4px; font-weight: 700; margin-top: 10px; }
  .brand-tagline {
    margin-top: 26px; font-weight: 700; font-size: 25px; line-height: 1.35; letter-spacing: 1.5px;
  }
</style>
</head>
<body>
<main class="sheet">

  <section class="card contact" aria-label="Business card, contact side">
    <svg class="card-art" viewBox="0 0 500 285" preserveAspectRatio="none" aria-hidden="true">
      <defs>
        <clipPath id="navy-area">
          <path d="M0,0 H500 C470,140 330,255 0,285 Z"/>
        </clipPath>
        <linearGradient id="curve-shade" x1="0" y1="0" x2="1" y2="1">
          <stop offset="0" stop-color="#000" stop-opacity="0.18"/>
          <stop offset="1" stop-color="#000" stop-opacity="0"/>
        </linearGradient>
      </defs>
      <rect width="500" height="285" fill="var(--paper)"/>
      <path d="M0,0 H500 C474,150 336,262 0,292 Z" fill="url(#curve-shade)"/>
      <g clip-path="url(#navy-area)">
        <rect width="500" height="285" fill="var(--navy)"/>
        <rect y="44" width="500" height="31" fill="var(--navy-band)"/>
        <rect y="75" width="500" height="3" fill="#15264a" opacity="0.5"/>
        <rect y="98" width="500" height="31" fill="var(--navy-band)"/>
        <rect y="129" width="500" height="3" fill="#15264a" opacity="0.5"/>
        <rect y="154" width="500" height="31" fill="var(--navy-band)"/>
        <rect y="185" width="500" height="3" fill="#15264a" opacity="0.5"/>
      </g>
      <g class="icon-mail" fill="none" stroke="var(--icon)" stroke-width="1.6">
        <rect x="32" y="52" width="24" height="16" rx="1"/>
        <path d="M32,52 L44,62 L56,52"/>
      </g>
      <g class="icon-web" fill="none" stroke="var(--icon)" stroke-width="1.4">
        <circle cx="44" cy="114" r="11"/>
        <ellipse cx="44" cy="114" rx="5" ry="11"/>
        <path d="M33,114 H55 M35,108 H53 M35,120 H53"/>
      </g>
      <path class="icon-phone" fill="var(--icon)"
        d="M35,162 c2,-2 5,-1 6,1 l2,4 c1,2 0,3 -2,4 c1,3 3,6 6,8 c1,-2 3,-3 5,-2 l3,2 c2,1 2,4 0,5 c-3,3 -7,2 -11,-1 c-5,-4 -9,-9 -10,-14 c-1,-3 0,-6 1,-7 z"/>
    </svg>

    <p class="contact-row email">jordan@brightwellconsulting.example</p>
    <p class="contact-row web">http://brightwellconsulting.example/</p>
    <p class="contact-row phone">555-014-2368</p>

    <div class="front-logo">
      <span class="logo-name">Brightwell</span>
      <span class="logo-sub">CONSULTING</span>
      <span class="front-tagline">Plan Well, Lead Well, Grow Well</span>
    </div>
  </section>

  <section class="card brand" aria-label="Business card, brand side">
    <span class="logo-name">Brightwell</span>
    <span class="logo-sub">CONSULTING</span>
    <p class="brand-tagline">Plan Well, Lead Well,<br>Grow Well</p>
  </section>

</main>
</body>
</html>
```